Design some Business Cards for Interior Contracting Firm

Design business cards for Contracting Firm. The design needs to be simple yet innovative and catchy.

Appreciate out-of-the-box thinking.

Name: Corvane Buildworks Private Limited.

A copy of the existing design is attached.

Revert for any questions.

```html
<!DOCTYPE html>
<html lang="en">
<head>
<meta charset="utf-8">
<title>Corvane Buildworks – Business Cards</title>
<link href="https://fonts.googleapis.com/css2?family=Lato:wght@400;700&display=swap" rel="stylesheet">
<style>
  :root {
    --brand-red: #d7262f;
    --ink-grey: #5a5a5a;
    --tab-grey: #6b6b6b;
    --card-white: #ffffff;
    --backdrop: #e9e6e1;
  }
  * { box-sizing: border-box; margin: 0; padding: 0; }
  html, body {
    width: 1200px; height: 1000px; overflow: hidden;
    background: var(--backdrop);
    font-family: "Lato", Arial, sans-serif;
  }
  .sheet {
    width: 1200px; height: 1000px;
    display: flex; flex-direction: column;
    align-items: center; justify-content: center; gap: 60px;
  }
  .card {
    position: relative;
    width: 700px; height: 400px;
    background: var(--card-white);
    box-shadow: 0 6px 18px rgba(0,0,0,0.18);
    overflow: hidden;
  }
  /* Front */
  .card-front { display: flex; align-items: center; justify-content: center; }
  .wordmark {
    display: flex; align-items: center; gap: 18px;
    color: var(--brand-red);
    font-weight: 700;
    text-transform: uppercase;
  }
  .wordmark-square { width: 44px; height: 44px; background: var(--brand-red); }
  .wordmark-name { font-size: 40px; letter-spacing: 2px; line-height: 1.15; }
  /* Back */
  .card-back { padding: 70px 0 0 90px; }
  .holder-name {
    color: var(--brand-red); font-weight: 700;
    font-size: 30px; letter-spacing: 0.5px; text-transform: uppercase;
  }
  .holder-title { color: var(--ink-grey); font-size: 22px; margin-top: 4px; }
  .contact-list { list-style: none; margin-top: 34px; font-size: 19px; color: var(--ink-grey); line-height: 1.45; }
  .contact-label { color: var(--brand-red); font-weight: 700; margin-right: 6px; }
  .company-name { color: var(--brand-red); font-weight: 700; font-size: 20px; margin-top: 22px; }
  .company-address { color: var(--ink-grey); font-size: 19px; margin-top: 2px; }
  .edge-strip { position: absolute; left: 0; bottom: 0; width: 100%; height: 34px; }
  .web-tab {
    position: absolute; left: 0; bottom: 0;
    width: 200px; height: 34px;
    background: var(--tab-grey); color: #fff;
    font-size: 15px; display: flex; align-items: center; justify-content: center;
  }
  .red-rule {
    position: absolute; left: 200px; bottom: 0;
    width: 260px; height: 8px; background: var(--brand-red);
  }
</style>
</head>
<body>
<main class="sheet">
  <section class="card card-front" aria-label="Business card front">
    <div class="wordmark">
      <span class="wordmark-square"></span>
      <span class="wordmark-name">Corvane Buildworks<br>Pvt. Ltd.</span>
    </div>
  </section>

  <section class="card card-back" aria-label="Business card back">
    <h1 class="holder-name">Arnav Kelkar</h1>
    <p class="holder-title">Director</p>
    <ul class="contact-list">
      <li><span class="contact-label">M:</span>+91 444 555</li>
      <li><span class="contact-label">F:</span>555 666 777</li>
      <li><span class="contact-label">E:</span>arnav.kelkar@corvane.com</li>
    </ul>
    <p class="company-name">Corvane Buildworks Pvt. Ltd.</p>
    <p class="company-address">12 Meridian Court, Lakeview, Pune 411001</p>
    <div class="edge-strip">
      <div class="web-tab">www.corvane.com</div>
      <div class="red-rule"></div>
    </div>
  </section>
</main>
</body>
</html>
```